Brevik Fabrication - Business Card Design

We would like a dark (likely black) themed business card to be able to hand out to potential clients. We may list our services on the card or keep it clean. Unsure. Logo attached

```html
<!DOCTYPE html>
<html lang="en">
<head>
<meta charset="utf-8">
<title>Brevik Fabrication – Business Cards</title>
<link href="https://fonts.googleapis.com/css2?family=Montserrat:wght@400;500;800&display=swap" rel="stylesheet">
<style>
  :root {
    --bg: #1a1a1a;
    --card: #202020;
    --ink: #ffffff;
    --orange: #f05a22;
    --blue: #2472c8;
  }
  * { margin: 0; padding: 0; box-sizing: border-box; }
  html, body { width: 1200px; height: 900px; overflow: hidden; background: var(--bg); }
  .canvas { position: relative; width: 1200px; height: 900px; background: var(--bg); font-family: "Montserrat", sans-serif; }
  .card {
    position: absolute; left: 250px; width: 700px; height: 400px;
    background: var(--card); overflow: hidden;
    box-shadow: 0 12px 30px rgba(0,0,0,.45);
  }
  .card--info { top: 35px; }
  .card--brand { top: 465px; }
  .card__stripes { position: absolute; inset: 0; width: 700px; height: 400px; }

  .person { position: absolute; left: 90px; top: 150px; color: var(--ink); }
  .person__name { font-weight: 800; font-size: 40px; letter-spacing: 1px; line-height: 1; }
  .person__role { font-weight: 400; font-size: 20px; margin: 8px 0 0 128px; letter-spacing: 1px; }

  .divider { position: absolute; left: 345px; top: 60px; width: 2px; height: 200px;
    background: linear-gradient(var(--blue), rgba(36,114,200,0)); }

  .contacts { position: absolute; left: 385px; top: 70px; list-style: none; }
  .contacts li { display: flex; align-items: center; gap: 16px; height: 40px;
    color: var(--ink); font-size: 15px; font-weight: 500; }
  .contacts svg { width: 26px; height: 26px; flex: none; }

  .mini-mark { position: absolute; left: 40px; top: 330px; display: flex; align-items: center; gap: 8px;
    color: var(--orange); font-weight: 800; font-size: 14px; letter-spacing: 1px; }
  .mini-mark__dot { width: 12px; height: 12px; border-radius: 50%; background: var(--blue); }

  .wordmark { position: absolute; left: 0; right: 0; top: 110px; text-align: center;
    color: var(--blue); font-weight: 800; letter-spacing: 2px; line-height: 1.05; }
  .wordmark__dot { display: block; width: 56px; height: 56px; border-radius: 50%;
    background: var(--orange); margin: 0 auto 18px; }
  .wordmark__main { font-size: 52px; display: block; }
  .wordmark__sub { font-size: 26px; display: block; margin-top: 6px; }
</style>
</head>
<body>
<main class="canvas">

  <section class="card card--info">
    <div class="divider"></div>
    <div class="person">
      <p class="person__name">JOHN DOE</p>
      <p class="person__role">CEO</p>
    </div>
    <ul class="contacts">
      <li><svg viewBox="0 0 26 26"><circle cx="13" cy="13" r="12" fill="#fff"/><path d="M9 7c1 0 2 2 2 3s-1 1-1 2c1 2 2 3 4 4 1 0 1-1 2-1s3 1 3 2-1 3-3 3c-4 0-9-5-9-9 0-2 1-4 2-4z" fill="#202020"/></svg>123 456 7890</li>
      <li><svg viewBox="0 0 26 26"><circle cx="13" cy="13" r="12" fill="#fff"/><path d="M13 6a5 5 0 0 0-5 5c0 4 5 9 5 9s5-5 5-9a5 5 0 0 0-5-5z" fill="#202020"/><circle cx="13" cy="11" r="2" fill="#fff"/></svg>Street-no 123, Place, City</li>
      <li><svg viewBox="0 0 26 26"><circle cx="13" cy="13" r="12" fill="#fff"/><circle cx="13" cy="13" r="6.5" fill="none" stroke="#202020" stroke-width="1.5"/><path d="M6.5 13h13M13 6.5c-3 3.5-3 9.5 0 13M13 6.5c3 3.5 3 9.5 0 13" fill="none" stroke="#202020" stroke-width="1.3"/></svg>www.website.com</li>
      <li><svg viewBox="0 0 26 26"><circle cx="13" cy="13" r="12" fill="#fff"/><rect x="7" y="9" width="12" height="8" fill="none" stroke="#202020" stroke-width="1.5"/><path d="M7 9l6 5 6-5" fill="none" stroke="#202020" stroke-width="1.5"/></svg>company@mail.com</li>
    </ul>
    <div class="mini-mark"><span class="mini-mark__dot"></span>BREVIK</div>
    <svg class="card__stripes" viewBox="0 0 700 400" aria-hidden="true">
      <path d="M0 366 H300 Q315 366 325 348 L330 340 Q336 332 350 332 H700 V346 H356 Q344 346 338 356 L332 366 Q322 380 306 380 H0 Z" fill="var(--orange)"/>
      <path d="M0 386 H310 Q328 386 338 368 L342 360 Q348 352 362 352 H700 V364 H368 Q356 364 350 374 L347 380 Q338 398 318 398 H0 Z" fill="var(--blue)"/>
    </svg>
  </section>

  <section class="card card--brand">
    <div class="wordmark">
      <span class="wordmark__dot"></span>
      <span class="wordmark__main">BREVIK</span>
      <span class="wordmark__sub">FABRICATION INC</span>
    </div>
    <svg class="card__stripes" viewBox="0 0 700 400" aria-hidden="true">
      <path d="M0 366 H300 Q315 366 325 348 L330 340 Q336 332 350 332 H700 V346 H356 Q344 346 338 356 L332 366 Q322 380 306 380 H0 Z" fill="var(--orange)"/>
      <path d="M0 386 H310 Q328 386 338 368 L342 360 Q348 352 362 352 H700 V364 H368 Q356 364 350 374 L347 380 Q338 398 318 398 H0 Z" fill="var(--blue)"/>
    </svg>
  </section>

</main>
</body>
</html>
```